Cedar Hollow Nectar Co.

Using the logo created by your designer I need to have a label made for retail sales of my product (Local Raw Honey) local and raw are the key phrases that would need to stand out to the consumer on the grocery shelves or farmers markets and that this is a 100% pure product. The label will also need to include Net weight in pounds and kg with space for me to write in the numerals as I have multiple size jars (I've included my home made label for reference on the Net weight requirements for my state) and I will need my business name and address "Cedar Holow Nectar Co. 4817 Wexley Rd SW South Danfield Mi. 49372" at the bottom of the of the label.

```html
<!DOCTYPE html>
<html lang="en">
<head>
<meta charset="utf-8">
<title>Cedar Hollow Nectar Co. – Wildflower Honey Label</title>
<link href="https://fonts.googleapis.com/css2?family=Old+Standard+TT:wght@400;700&family=Special+Elite&display=swap" rel="stylesheet">
<style>
  :root {
    --paper: #f3dcae;
    --paper-edge: #e6a66c;
    --paper-rim: #de8c58;
    --ticket: #efdcae;
    --rule: #4a2a22;
    --ink: #351218;
    --red: #c1202b;
    --copper-1: #b4532a;
    --copper-2: #e2884f;
    --copper-3: #9b3818;
    --copper-4: #c46a36;
    --charcoal: #232323;
    --badge: #e2dccb;
  }
  * { box-sizing: border-box; margin: 0; padding: 0; }
  html, body { width: 1200px; height: 873px; overflow: hidden; background: #fff; }
  body { position: relative; font-family: "Old Standard TT", serif; }

  .label {
    position: absolute; left: 224px; top: 170px; width: 753px; height: 527px;
    overflow: hidden;
    background:
      radial-gradient(ellipse 70% 60% at 45% 40%, var(--paper) 45%, rgba(243,220,174,0) 100%),
      linear-gradient(180deg, var(--paper-rim) 0, var(--paper-edge) 14px, #efc48e 40px, #efc48e 100%);
    box-shadow: 0 2px 6px rgba(0,0,0,.18);
  }
  .band-copper {
    position: absolute; left: 0; right: 0; top: 381px; height: 34px;
    background: linear-gradient(90deg, var(--copper-1) 0, var(--copper-2) 44%, var(--copper-3) 58%, var(--copper-4) 100%);
  }
  .band-dark { position: absolute; left: 0; right: 0; top: 415px; bottom: 0; background: var(--charcoal); }

  .brand { position: absolute; left: 0; right: 0; top: 14px; text-align: center; }
  .brand-dot { width: 62px; height: 62px; border-radius: 50%; background: var(--badge); margin: 14px auto 10px; }
  .brand-name { font-size: 21px; font-weight: 700; color: var(--ink); letter-spacing: .5px; }

  .variety {
    position: absolute; left: 0; right: 0; top: 150px; text-align: center;
    color: var(--red); font-size: 39px; letter-spacing: 8px; padding-left: 10px;
  }
  .product {
    position: absolute; left: 0; right: 0; top: 178px; text-align: center;
    color: var(--ink); font-size: 92px; letter-spacing: 17px; padding-left: 26px; line-height: 1.1;
  }
  .tagline {
    position: absolute; left: 0; right: 0; top: 268px; text-align: center;
    color: var(--red); font-family: "Special Elite", monospace; font-size: 18px; letter-spacing: 2px; padding-left: 14px;
  }

  .ticket { position: absolute; left: 168px; top: 308px; width: 424px; height: 208px; }
  .ticket svg { position: absolute; inset: 0; }
  .frame {
    position: absolute; left: 22px; top: 18px; width: 382px; height: 176px;
    border: 1px solid var(--rule);
  }
  .row { position: absolute; left: 0; right: 0; border-bottom: 1px solid var(--rule); }
  .row-origin { top: 0; height: 77px; }
  .row-weight { top: 77px; height: 34px; }
  .row-maker { top: 111px; height: 42px; }
  .row-note { top: 153px; height: 22px; border-bottom: 0; }

  .state-map { position: absolute; left: 16px; top: 24px; width: 32px; height: 34px; background: #1e1e1e; border-radius: 3px; }
  .origin-text {
    position: absolute; left: 62px; top: 27px; width: 192px;
    font-family: "Special Elite", monospace; font-size: 12.5px; line-height: 15px; color: var(--ink);
  }
  .flower-art {
    position: absolute; left: 255px; top: 0; right: 0; bottom: 0;
    border-left: 1px solid var(--rule);
    background: radial-gradient(circle at 55% 65%, #e98a4e 0, #f0b483 28%, #efd6a8 70%);
  }
  .weight {
    text-align: center; font-family: "Special Elite", monospace; font-size: 20px;
    letter-spacing: 2px; line-height: 34px; color: var(--ink);
  }
  .maker { text-align: center; padding-top: 4px; }
  .maker-name { color: var(--red); font-size: 12.5px; line-height: 16px; }
  .maker-address { color: var(--ink); font-size: 13.5px; line-height: 18px; }
  .note { padding: 3px 0 0 11px; font-size: 6.6px; line-height: 8.5px; color: var(--ink); }
</style>
</head>
<body>
  <main class="label">
    <div class="band-copper"></div>
    <div class="band-dark"></div>

    <header class="brand">
      <div class="brand-dot"></div>
      <div class="brand-name">Cedar Hollow Nectar Co.</div>
    </header>

    <div class="variety">WILDFLOWER</div>
    <h1 class="product" style="font-weight:400">HONEY</h1>
    <p class="tagline">PURE. RAW. NATURAL.</p>

    <section class="ticket">
      <svg viewBox="0 0 424 208" width="424" height="208" aria-hidden="true">
        <polygon fill="var(--ticket)" points="10,0 0,12 10,24 0,36 10,48 0,60 10,72 0,84 10,96 0,108 10,120 0,132 10,144 0,156 10,168 0,180 10,192 0,204 10,208 414,208 424,204 414,192 424,180 414,168 424,156 414,144 424,132 414,120 424,108 414,96 424,84 414,72 424,60 414,48 424,36 414,24 424,12 414,0"/>
      </svg>
      <div class="frame">
        <div class="row row-origin">
          <div class="state-map" role="img" aria-label="Silhouette map of Michigan"></div>
          <p class="origin-text">BROUGHT TO YOU BY LOCAL<br>MICHIGAN BEE’S</p>
          <div class="flower-art" role="img" aria-label="Copper line illustration of a wildflower"></div>
        </div>
        <div class="row row-weight"><p class="weight">NET WT. 16 OZ (.45 KG)</p></div>
        <div class="row row-maker">
          <p class="maker-name">CEDAR HOLOW NECTAR CO.</p>
          <p class="maker-address">4817 WEXLEY RD SW SOUTH DANFIELD MI. 49372</p>
        </div>
        <div class="row row-note">
          <p class="note">DISCLAIMER: PROCESSED IN A FACILITY NOT INSPECTED BY THE DEPARTMENT OF AGRICULTURE &amp;<br>RURAL DEVELOPMENT • MINIMALLLY FILTERED • ALL PACKAGING PRODUCED IN THE USA</p>
        </div>
      </div>
    </section>
  </main>
</body>
</html>
```